Need Power Point Presentation - That incorporates New Logo

We have a new logo and would like to incorporate it into a Power Point template. We are looking for title page, 2 body pages and a closing page design. If you have any questions please let me know. New logo is attached.

```html
<!DOCTYPE html>
<html lang="en">
<head>
<meta charset="utf-8">
<title>Thanks For Listening</title>
<link href="https://fonts.googleapis.com/css2?family=Source+Sans+3:wght@700&family=Montserrat:wght@400&display=swap" rel="stylesheet">
<style>
  :root {
    --sky-top: #00b7ff;
    --sky-mid: #1cc2ff;
    --sky-glow: #a6e4fb;
    --wave-light: rgba(190, 236, 255, 0.55);
    --white: #ffffff;
  }
  html, body {
    margin: 0;
    padding: 0;
    width: 1200px;
    height: 900px;
    overflow: hidden;
  }
  .slide {
    position: relative;
    width: 1200px;
    height: 900px;
    overflow: hidden;
    background:
      radial-gradient(ellipse 700px 520px at 820px 900px, var(--sky-glow) 0%, rgba(166,228,251,0.5) 40%, rgba(28,194,255,0) 80%),
      linear-gradient(180deg, var(--sky-top) 0%, var(--sky-top) 50%, var(--sky-mid) 100%);
  }
  .wave-decoration {
    position: absolute;
    left: 0;
    bottom: 0;
    width: 1200px;
    height: 420px;
    background:
      radial-gradient(ellipse 520px 260px at 300px 420px, var(--wave-light) 0%, rgba(190,236,255,0.25) 45%, rgba(190,236,255,0) 80%),
      radial-gradient(ellipse 420px 120px at 1000px 420px, rgba(120,190,220,0.35) 0%, rgba(120,190,220,0) 80%);
  }
  .closing {
    position: absolute;
    top: 338px;
    left: 0;
    width: 100%;
    text-align: center;
    color: var(--white);
  }
  .closing-title {
    margin: 0;
    font-family: "Source Sans 3", sans-serif;
    font-weight: 700;
    font-size: 71px;
    line-height: 1;
    letter-spacing: -0.5px;
  }
  .closing-byline {
    margin: 24px 0 0;
    font-family: "Montserrat", sans-serif;
    font-weight: 400;
    font-size: 23px;
    letter-spacing: 0.6px;
  }
</style>
</head>
<body>
<main class="slide">
  <div class="wave-decoration" role="img" aria-label="Sweeping bundle of fine white wave lines across the lower left, fading into a soft blue ribbon at the bottom right"></div>
  <section class="closing">
    <h1 class="closing-title">Thanks For Listening</h1>
    <p class="closing-byline">John Doe, 1 January 2014</p>
  </section>
</main>
</body>
</html>
```